Business Card Design Project

Beauty Therapist
Bold, bright, feminine, like contrast, love flowers, girly stuff. Must be beautiful. But open to all suggestions. Business name: Plush Clover.
xxx
Danuta Kaczmarczyk
Updates

Project Deadline Extended
Reason: I think you need more time to design something good. X

Target Market(s)

ignore this

Industry/Entity Type

Business

```html
<!DOCTYPE html>
<html lang="en">
<head>
<meta charset="utf-8">
<title>Plush Clover – Business Card</title>
<link rel="stylesheet" href="https://fonts.googleapis.com/css2?family=Dancing+Script:wght@500&family=Quicksand:wght@400&display=swap">
<style>
  :root {
    --backdrop: #474747;
    --card: #ffffff;
    --card-blush: #fbe6f0;
    --magenta: #e0117f;
    --ink: #1a1a1a;
    --art-main: #f6b9d6;
    --art-soft: #fbe0ec;
  }
  * { box-sizing: border-box; margin: 0; padding: 0; }
  html, body {
    width: 1027px; height: 1200px; overflow: hidden;
    background: var(--backdrop);
  }
  .sheet { position: relative; width: 1027px; height: 1200px; }
  .card {
    position: absolute; left: 33px; width: 960px; height: 555px;
    overflow: hidden;
    background: linear-gradient(160deg, var(--card) 35%, var(--card-blush) 100%);
    box-shadow: 0 3px 10px rgba(0,0,0,0.45);
  }
  .card--front { top: 28px; }
  .card--back {
    top: 611px;
    background: linear-gradient(200deg, var(--card) 35%, var(--card-blush) 100%);
  }

  .artwork { position: absolute; }
  .card--front .artwork {
    left: 0; top: 250px; width: 440px; height: 305px;
    background: linear-gradient(90deg, var(--art-main) 0%, var(--art-soft) 55%, rgba(251,224,236,0) 100%);
  }
  .card--back .artwork {
    right: 0; top: 255px; width: 440px; height: 300px;
    background: linear-gradient(270deg, var(--art-main) 0%, var(--art-soft) 55%, rgba(251,224,236,0) 100%);
  }

  .text { position: absolute; left: 0; width: 100%; text-align: center; line-height: 1; }
  .brand-title {
    font-family: "Dancing Script", cursive; font-weight: 500;
    color: var(--magenta); font-size: 132px; top: 92px;
  }
  .role {
    font-family: "Quicksand", sans-serif; font-weight: 400;
    color: var(--ink); letter-spacing: 0.06em;
  }
  .card--front .role { font-size: 58px; top: 292px; }
  .person {
    font-family: "Dancing Script", cursive; font-weight: 500;
    color: var(--magenta); font-size: 88px; top: 68px;
  }
  .card--back .role { font-size: 49px; top: 184px; }
  .phone {
    font-family: "Dancing Script", cursive; font-weight: 500;
    color: var(--magenta); font-size: 74px; top: 258px;
  }
  .brand-sign {
    font-family: "Dancing Script", cursive; font-weight: 500;
    color: var(--magenta); font-size: 80px; top: 432px;
  }
</style>
</head>
<body>
<main class="sheet">
  <section class="card card--front">
    <div class="artwork" role="img" aria-label="Pink floral illustration with soft swirls"></div>
    <h1 class="text brand-title">Plush Clover</h1>
    <p class="text role">BEAUTY THERAPIST</p>
  </section>

  <section class="card card--back">
    <div class="artwork" role="img" aria-label="Pink floral illustration with soft swirls"></div>
    <h2 class="text person">Danuta Kaczmarczyk</h2>
    <p class="text role">BEAUTY THERAPIST</p>
    <p class="text phone">020 7946 0321</p>
    <p class="text brand-sign">Plush Clover</p>
  </section>
</main>
</body>
</html>
```